Tropic Ramble Co Business Website Branding

Looking for a wordpress template design with CSS and HTML encoding. Current website can be seen at tropicrambleco.net.

WE ARE CURRENTLY IN PROCESS GETTING A LOGO DESIGN... I HAVE INCLUDED THE TOP POTENTIAL DESIGNS FOR REFERENCE TO HELP UNDERSTAND WHAT STYLE WE ARE LOOKING FOR...
NOTE: THE “SWAMP DOODLES” LOGO WAS A PREVIOUS COMPANY WE OWNED SO YOU CAN GE A FEEL FOR THE TYPE OF DESIGNS WE HAVE USED IN THE PAST.

My blog will focus on making a connection with wild Florida, it’s wildlife, plants and animals... with an eye toward Florida conservation, nature adventure trips, and education... Content, photos and other merchandise will also be offered for sale.
I’m looking for a site design that incorporates Florida nature and wildlife/plants, with a fun “Old Florida” retro-adventure feel.
When they see this site it should speak to the import of natural Florida and the critical nature of the ecosystem here... while being instantly recognizable and iconic... IE: when I think of florida I think of water, plants, warmth, sunsets etc...

https://join.teamhubzo.net/t/ravenbyte-xqk2281/shared_invite/zt-pmqvr83x-aLmNo4PqRsTuVw6xYzBcDe

Target Market(s)

Nature, Education, Conservation, Photography

Industry/Entity Type

Photographer

Coding

Coded - Design and coding required

Requirements
Must have
• Need to have site wide template design which generally includes a landing page and a general page template for other pages... Must include html and css encoding...
Should not have
• Any animals included in the site should be Florida native... IE: no African animals etc... This will require some research to ensure that if animals are included that they are part of the Florida ecosystem.

```html
<!DOCTYPE html>
<html lang="en">
<head>
<meta charset="utf-8">
<title>Tropic Ramble Co</title>
<link rel="stylesheet" href="https://fonts.googleapis.com/css2?family=Roboto:wght@400;500;700&family=Allura&display=swap">
<style>
:root{
  --paper:#e8c590;
  --paper-dark:#d9b07a;
  --header:#f3d3a0;
  --orange:#f07a12;
  --orange-deep:#e2531a;
  --red:#c8322a;
  --red-deep:#a9221d;
  --ink:#1f1a16;
  --text:#3a2e24;
  --muted:#8a7460;
  --card:#f8d49a;
  --navy:#121829;
  --white:#ffffff;
}
*{margin:0;padding:0;box-sizing:border-box}
html,body{width:1200px;height:3994px;overflow:hidden}
body{position:relative;background:var(--paper);font-family:"Roboto",Arial,sans-serif;color:var(--text)}
.abs{position:absolute}
.script{font-family:"Allura",cursive;font-weight:400;color:var(--ink)}
.btn{position:absolute;display:flex;align-items:center;justify-content:center;border-radius:26px;background:linear-gradient(90deg,var(--orange-deep),var(--orange));color:var(--white);font-weight:700;font-size:14px;letter-spacing:.2px;box-shadow:0 3px 6px rgba(0,0,0,.2)}
.btn .arrow{display:inline-block;width:13px;height:13px;border-radius:50%;background:var(--white);margin-left:5px;position:relative}
.btn .arrow:after{content:"";position:absolute;left:3px;top:4px;border-left:6px solid var(--orange-deep);border-top:3px solid transparent;border-bottom:3px solid transparent}

/* header */
.site-header{position:absolute;left:0;top:0;width:1200px;height:152px;background:var(--header);border-top:3px solid var(--orange)}
.brand{position:absolute;left:115px;top:46px;display:flex;align-items:center;gap:12px}
.brand-dot{width:34px;height:34px;border-radius:50%;background:var(--orange)}
.brand-name{font-size:30px;font-weight:700;color:var(--ink)}
.cart-btn{position:absolute;left:941px;top:28px;width:50px;height:50px;border-radius:50%;background:var(--orange-deep);box-shadow:0 2px 5px rgba(0,0,0,.25)}
.cart-divider{position:absolute;left:1012px;top:30px;width:1px;height:44px;background:#8d7153}
.cart-label{position:absolute;left:1032px;top:30px;font-size:13px;color:#5b4a3a}
.cart-total{position:absolute;left:1032px;top:48px;font-size:22px;font-weight:700;color:#3a2e24}
.main-nav{position:absolute;top:104px;left:622px;display:flex;gap:0;font-size:14px;color:#2b231c}
.main-nav a{color:inherit;text-decoration:none;position:absolute;white-space:nowrap}
.main-nav .active{color:var(--orange-deep)}
.main-nav .active:after{content:"";position:absolute;left:0;right:0;top:22px;height:2px;background:var(--orange-deep)}

/* hero */
.hero{position:absolute;left:0;top:152px;width:1200px;height:640px;background:linear-gradient(180deg,#4d88d4 0%,#8fb6e0 25%,#6e8a5a 55%,#3d6a2c 80%,#2f5222 100%)}
.hero-panel{position:absolute;left:395px;top:155px;width:420px;height:155px;background:rgba(90,110,130,.35)}
.hero-title{position:absolute;left:0;width:1200px;top:168px;text-align:center;font-size:78px;color:var(--white);line-height:1}
.hero-copy{position:absolute;left:390px;width:420px;top:258px;text-align:center;font-size:14px;line-height:26px;color:var(--white)}
.hero-dots{position:absolute;left:568px;top:496px;display:flex;gap:8px;align-items:center}
.hero-dots span{display:block;border:2px solid var(--white);border-radius:50%}

/* welcome */
.welcome-title{position:absolute;left:0;width:1200px;top:840px;text-align:center;font-size:80px;line-height:1}
.welcome-copy{position:absolute;left:185px;width:830px;top:940px;text-align:center;font-size:14.5px;line-height:26px;color:#3b2f24}
.photo-circle{position:absolute;width:262px;height:262px;border-radius:50%;border:4px solid #f2d09c}

/* about */
.about-photo{position:absolute;left:140px;top:1590px;width:400px;height:420px;border-radius:46% 54% 48% 52% / 50% 44% 56% 50%;background:linear-gradient(160deg,#c9703a 0%,#e6b48a 40%,#4aa5b8 70%,#2f7f94 100%)}
.about-title{position:absolute;left:585px;top:1570px;font-size:84px;color:var(--white);line-height:1}
.about-copy{position:absolute;left:587px;width:446px;top:1667px;font-size:14.5px;line-height:25.8px;color:var(--white);text-align:justify}

/* gallery */
.gallery-title{position:absolute;left:0;width:1200px;top:2170px;text-align:center;font-size:80px;line-height:1}
.gallery-item{position:absolute;box-shadow:0 2px 6px rgba(0,0,0,.25)}

/* blog */
.blog-title{position:absolute;left:0;width:1200px;top:2850px;text-align:center;font-size:84px;line-height:1}
.blog-card{position:absolute;left:112px;top:2970px;width:976px;height:375px;background:var(--card);box-shadow:0 3px 8px rgba(0,0,0,.2)}
.blog-image{position:absolute;left:6px;top:6px;width:415px;height:362px;background:linear-gradient(160deg,#5f8f3e 0%,#6fa146 45%,#d64a1e 60%,#4a7a2f 100%)}
.blog-heading{position:absolute;left:469px;top:45px;width:460px;font-size:26px;font-weight:500;line-height:34px;color:#1c1712}
.blog-date{position:absolute;left:469px;top:150px;font-size:14px;color:var(--orange-deep);display:flex;align-items:center;gap:8px}
.blog-excerpt{position:absolute;left:469px;top:183px;width:460px;font-size:13.5px;line-height:26px;color:var(--muted)}
.slider-arrow{position:absolute;width:50px;height:50px;border-radius:50%;background:var(--red);top:3132px}

/* footer */
.site-footer{position:absolute;left:0;top:3500px;width:1200px;height:494px}
.footer-bg{position:absolute;left:0;top:0}
.footer-head{position:absolute;top:148px;font-size:17px;font-weight:500;color:var(--white)}
.footer-links{position:absolute;left:105px;top:196px;list-style:none;font-size:13px;color:var(--white)}
.footer-links li{height:32.5px;display:flex;align-items:center;gap:14px}
.footer-links li:before{content:"»";font-size:13px}
.contact-row{position:absolute;left:273px;display:flex;align-items:center;gap:17px;font-size:12.5px;line-height:19px;color:var(--white)}
.contact-icon{width:36px;height:36px;border-radius:50%;border:2px solid var(--white);flex:none;display:flex;align-items:center;justify-content:center}
.story-copy{position:absolute;left:607px;top:186px;width:485px;font-size:13px;line-height:24px;color:var(--white)}
.copyright{position:absolute;left:105px;top:440px;font-size:12px;color:var(--white)}
.social{position:absolute;top:434px;width:30px;height:30px;border-radius:50%;border:1.5px solid var(--white)}
</style>
</head>
<body>

<header class="site-header">
  <div class="brand"><span class="brand-dot"></span><span class="brand-name">Tropic Ramble Co</span></div>
  <div class="cart-btn">
    <svg width="50" height="50" viewBox="0 0 50 50"><path d="M18 19h3l2 9h9l2-7H22" fill="none" stroke="#fff" stroke-width="2"/><circle cx="24" cy="31" r="1.6" fill="#fff"/><circle cx="31" cy="31" r="1.6" fill="#fff"/></svg>
  </div>
  <div class="cart-divider"></div>
  <div class="cart-label">My Cart :</div>
  <div class="cart-total">$0.00</div>
  <nav class="main-nav">
    <a class="active" style="left:0">HOME</a>
    <a style="left:74px">ABOUT</a>
    <a style="left:153px">SERVICES</a>
    <a style="left:251px">BLOG</a>
    <a style="left:320px">FAQ</a>
    <a style="left:378px">CONTACT US</a>
  </nav>
</header>

<section class="hero" role="img" aria-label="Photo of tall slash pines and palmetto scrub under a blue sky">
  <div class="hero-panel"></div>
  <h1 class="hero-title script">Tropic Ramble Co</h1>
  <p class="hero-copy">Lorem ipsum dolor sit amet, consectetur adipiscing elit, sed do tempor incididunt ut labore et dolore magna aliqua.</p>
  <div class="btn" style="left:519px;top:323px;width:162px;height:49px">GET STARTED</div>
  <div class="hero-dots">
    <span style="width:17px;height:17px"></span>
    <span style="width:12px;height:12px"></span>
    <span style="width:12px;height:12px"></span>
  </div>
</section>

<svg class="abs" style="left:0;top:600px" width="1200" height="200" viewBox="0 600 1200 200">
  <path d="M0 712 C150 730 300 770 520 762 C760 752 900 610 1100 628 C1150 632 1180 645 1200 655 L1200 800 L0 800 Z" fill="var(--paper)"/>
  <path d="M0 712 C150 730 300 770 520 762 C760 752 900 610 1100 628 C1150 632 1180 645 1200 655" fill="none" stroke="var(--red)" stroke-width="5"/>
  <path d="M0 719 C150 737 300 778 520 770 C760 760 900 618 1100 636 C1150 640 1180 652 1200 662" fill="none" stroke="#2a1a12" stroke-width="2" opacity=".6"/>
</svg>

<section class="welcome">
  <h2 class="welcome-title script">Welcome</h2>
  <p class="welcome-copy">Come explore wild places and stunning scenery with me as I discover new and exciting eco-adventures and learn about the rare and unique wildlife and environments that make Florida so precious and extraordinary. I hope you can vicariously enjoy the wild and untamed beauty of Florida through my eyes, and learn some amazing things about nature on our explorations.</p>
  <div class="btn" style="left:519px;top:1040px;width:162px;height:49px">LEARN MORE <span class="arrow"></span></div>

  <svg class="abs" style="left:0;top:1090px" width="1200" height="320" viewBox="0 1090 1200 320">
    <path d="M0 1244 H118 A155 155 0 0 0 428 1248" fill="none" stroke="#111" stroke-width="4"/>
    <circle cx="428" cy="1248" r="8" fill="#111"/><circle cx="428" cy="1248" r="4" fill="var(--orange)"/>
    <path d="M1200 1248 H1080 A155 155 0 0 0 770 1248" fill="none" stroke="#111" stroke-width="4"/>
    <circle cx="770" cy="1248" r="8" fill="#111"/><circle cx="770" cy="1248" r="4" fill="var(--orange)"/>
  </svg>
  <div class="photo-circle" role="img" aria-label="Photo of a tiny dark tree frog held on a fingertip" style="left:142px;top:1117px;background:radial-gradient(circle at 40% 60%,#e9b8a4 0%,#d99a88 35%,#5f8a4e 70%,#3f6b35 100%)"></div>
  <div class="photo-circle" role="img" aria-label="Photo of a white peacock butterfly on dry leaves" style="left:469px;top:1117px;background:radial-gradient(circle at 50% 50%,#efe8dc 0%,#b89a72 40%,#5c4630 80%,#3d2e20 100%)"></div>
  <div class="photo-circle" role="img" aria-label="Photo of an air plant with red bloom on a tree trunk" style="left:794px;top:1117px;background:linear-gradient(135deg,#7d9a5a 0%,#5f7d44 40%,#a9a093 70%,#6d6459 100%)"></div>
</section>

<svg class="abs" style="left:0;top:1480px" width="1200" height="630" viewBox="0 1480 1200 630">
  <path d="M0 1520 C300 1480 600 1475 880 1500 C1020 1512 1120 1530 1200 1550 L1200 2050 C900 2105 400 2110 0 2040 Z" fill="#f2c88c"/>
  <path d="M0 1530 C300 1492 600 1488 880 1512 C1020 1524 1120 1542 1200 1562 L1200 2038 C900 2093 400 2098 0 2028 Z" fill="var(--red)"/>
</svg>
<section class="about">
  <div class="about-photo" role="img" aria-label="Portrait photo of the author wearing sunglasses by the sea"></div>
  <h2 class="about-title script">About Me</h2>
  <p class="about-copy">Hello nature lovers! I’m Marisol Trent, a wildlife educator, Coastal Field Naturalist, nature writer and photographer, busy mama of three kiddos, a playful Havanese puppy, two very chubby guinea pigs, and a giant tree frog. I have a passion for all things nature and I adore living in Southwest Florida. I will always be a California girl, but from the moment I set foot in Florida, its wild beauty stole my heart. For the past 23 years, I have been fortunate to have some very unique and special experiences caring for many different species of animals and educating the public about wildlife and the environment. My hope is that those I endeavor to educate will better understand their connection with the natural world and our shared responsibility to protect Florida’s wild and priceless beauty.</p>
</section>

<section class="gallery">
  <h2 class="gallery-title script">Tropic Ramble Co Gallery</h2>
  <div class="gallery-item" role="img" aria-label="Photo of cabbage palms in a burned pine forest" style="left:112px;top:2283px;width:313px;height:225px;background:linear-gradient(180deg,#8aa3bf 0%,#56683f 50%,#3b3a28 100%)"></div>
  <div class="gallery-item" role="img" aria-label="Photo of tall pines over saw palmetto under cloudy sky" style="left:443px;top:2283px;width:314px;height:470px;background:linear-gradient(180deg,#b9cde0 0%,#8fb0c8 40%,#5c7a48 70%,#3b6a2a 100%)"></div>
  <div class="gallery-item" role="img" aria-label="Close-up photo of an orange lily flower" style="left:775px;top:2283px;width:313px;height:225px;background:linear-gradient(135deg,#e84a1c 0%,#f3862a 45%,#7a9a3a 100%)"></div>
  <div class="gallery-item" role="img" aria-label="Photo of pink apple snail eggs on a plant stem" style="left:112px;top:2528px;width:313px;height:225px;background:linear-gradient(135deg,#2f5a22 0%,#5a9a3a 45%,#d88aa8 55%,#1f2e18 100%)"></div>
  <div class="gallery-item" role="img" aria-label="Photo of an alligator among branches and Spanish moss" style="left:775px;top:2528px;width:313px;height:225px;background:linear-gradient(135deg,#5a7a4a 0%,#a8aba0 45%,#6c6a5c 100%)"></div>
</section>

<section class="blog">
  <h2 class="blog-title script">latest blog posts</h2>
  <div class="slider-arrow" style="left:84px"><svg width="50" height="50" viewBox="0 0 50 50"><path d="M28 17l-8 8 8 8" fill="none" stroke="#fff" stroke-width="3"/></svg></div>
  <div class="slider-arrow" style="left:1061px"><svg width="50" height="50" viewBox="0 0 50 50"><path d="M22 17l8 8-8 8" fill="none" stroke="#fff" stroke-width="3"/></svg></div>
  <article class="blog-card">
    <div class="blog-image" role="img" aria-label="Photo of a red pine lily in green grass"></div>
    <h3 class="blog-heading">Coastal Field Naturalist Uplands Nature Journal</h3>
    <div class="blog-date"><svg width="14" height="14" viewBox="0 0 14 14"><rect x="1" y="2" width="12" height="11" fill="none" stroke="currentColor" stroke-width="1.5"/><rect x="1" y="2" width="12" height="3" fill="currentColor"/></svg>September 24th-October 22nd, 2020</div>
    <p class="blog-excerpt">September 24th-October 22nd, 2020 Communing with Nature at Heron Hollow Preserve Trails*All photography by Marisol Trent, October 2020 Since I was...</p>
    <div class="btn" style="left:471px;top:285px;width:162px;height:49px">LEARN MORE <span class="arrow"></span></div>
  </article>
</section>

<footer class="site-footer">
  <svg class="footer-bg" width="1200" height="494" viewBox="0 0 1200 494">
    <path d="M0 40 C200 70 350 90 520 70 C760 40 980 -10 1200 40 L1200 494 L0 494 Z" fill="var(--navy)"/>
    <path d="M0 30 C200 60 350 80 520 60 C760 30 980 -20 1200 30" fill="none" stroke="var(--red)" stroke-width="10"/>
    <path d="M0 42 C200 72 350 92 520 72 C760 42 980 -8 1200 42" fill="none" stroke="#2a1010" stroke-width="3"/>
    <rect x="0" y="150" width="1200" height="344" fill="#0d1322" opacity=".4"/>
    <line x1="90" y1="405" x2="1110" y2="405" stroke="#3a4256" stroke-width="1"/>
  </svg>
  <div class="footer-head" style="left:105px">Useful Links</div>
  <ul class="footer-links">
    <li>Home</li><li>About me</li><li>Service</li><li>About</li><li>FAQ</li><li>Contact us</li>
  </ul>
  <div class="footer-head" style="left:273px">Contact Information</div>
  <div class="contact-row" style="top:188px"><span class="contact-icon"><svg width="14" height="18" viewBox="0 0 14 18"><path d="M7 1a6 6 0 0 0-6 6c0 4 6 10 6 10s6-6 6-10a6 6 0 0 0-6-6z" fill="none" stroke="#fff" stroke-width="1.6"/><circle cx="7" cy="7" r="2" fill="#fff"/></svg></span><span>Lorem ipsum dolor sit amet, conse<br>ctetur adipiscing elit</span></div>
  <div class="contact-row" style="top:240px"><span class="contact-icon"><svg width="16" height="16" viewBox="0 0 16 16"><path d="M3 1l3 3-2 2c1 2 3 4 5 5l2-2 3 3-2 3C7 15 1 9 1 3z" fill="#fff"/></svg></span><span>Phone : +1 888 888 8888</span></div>
  <div class="contact-row" style="top:286px"><span class="contact-icon"><svg width="16" height="12" viewBox="0 0 16 12"><rect width="16" height="12" rx="1" fill="#fff"/><path d="M1 1l7 6 7-6" fill="none" stroke="#121829" stroke-width="1.5"/></svg></span><span>Email : info@companyname.com</span></div>
  <div class="contact-row" style="top:339px"><span class="contact-icon"><svg width="14" height="16" viewBox="0 0 14 16"><rect x="1" y="5" width="12" height="10" fill="#fff"/><rect x="4" y="1" width="6" height="5" fill="none" stroke="#fff" stroke-width="1.5"/></svg></span><span>Fax: 0661-23045</span></div>
  <div class="footer-head" style="left:607px">Our Story :</div>
  <p class="story-copy">Lorem ipsum dolor sit amet, consectetur adipiscing elit, sed do eiusmod tempor incididunt ut labore et dolore magna aliqua. Ut enim ad minim veniam, quis nostrud exercitation ullamco laboris nisi ut aliquip ex ea commodo consequat. Duis aute irure dolor in reprehenderit in voluptate velit esse cillum dolore eu fugiat nulla pariatur. Excepteur sint occaecat cupidatat non proident, sunt in culpa qui officia deserunt mollit anim id est laborum.</p>
  <div class="copyright">Copyrights © 2020, Company Name. All rights reserved &nbsp;|&nbsp; Privacy policy</div>
  <span class="social" style="left:978px"></span>
  <span class="social" style="left:1015px;background:var(--red)"></span>
  <span class="social" style="left:1052px"></span>
</footer>

</body>
</html>
```